The Perfect Business Card for PineHarbor

I am looking for a business card which beautifully incorporates my logo, reflects my business and looks special, elegant and clean.

```html
<!DOCTYPE html>
<html lang="en">
<head>
<meta charset="utf-8">
<title>PineHarbor Business Card</title>
<link rel="stylesheet" href="https://fonts.googleapis.com/css2?family=Montserrat:wght@400;500;600;700&display=swap">
<style>
  :root {
    --page: #ffffff;
    --card-dark: #212a14;
    --card-mid: #28351a;
    --card-glow: #76a043;
    --panel: #4a6129;
    --accent: #6f9a3a;
    --accent-soft: rgba(111, 154, 58, 0.55);
    --text-light: #ffffff;
    --rule: rgba(255, 255, 255, 0.6);
    --shadow: rgba(0, 0, 0, 0.28);
  }
  * { margin: 0; padding: 0; box-sizing: border-box; }
  html, body {
    width: 800px;
    height: 1200px;
    overflow: hidden;
    background: var(--page);
    font-family: "Montserrat", sans-serif;
  }
  .canvas { position: relative; width: 800px; height: 1200px; }
  .card {
    position: absolute;
    left: 60px;
    width: 680px;
    height: 389px;
    overflow: hidden;
    box-shadow: 0 10px 28px var(--shadow);
  }
  .card--front {
    top: 181px;
    background:
      radial-gradient(ellipse 420px 300px at 100% 0%, var(--card-glow) 0%, rgba(80, 110, 45, 0.55) 40%, rgba(33, 42, 20, 0) 100%),
      var(--card-dark);
  }
  .card--back { top: 630px; background: var(--card-mid); }
  .card svg.shapes { position: absolute; inset: 0; width: 100%; height: 100%; }

  .brand {
    position: absolute;
    display: flex;
    align-items: center;
    color: var(--accent);
    font-weight: 500;
    letter-spacing: 0.01em;
  }
  .brand__mark {
    border: 2px solid var(--accent);
    border-radius: 50%;
    flex: none;
  }
  .card--front .brand { left: 45px; top: 103px; font-size: 50px; gap: 18px; }
  .card--front .brand__mark { width: 144px; height: 144px; }
  .card--back .brand { left: 47px; top: 61px; font-size: 32px; gap: 12px; }
  .card--back .brand__mark { width: 94px; height: 94px; }

  .motif {
    position: absolute;
    border-radius: 40px;
    background: linear-gradient(180deg, rgba(111, 154, 58, 0.08), rgba(111, 154, 58, 0.22));
  }
  .card--front .motif { left: 537px; top: 68px; width: 122px; height: 321px; }
  .card--back .motif { left: 102px; top: 172px; width: 92px; height: 217px; }

  .web-address {
    position: absolute;
    left: 47px;
    top: 302px;
    font-size: 18px;
    letter-spacing: 0.16em;
    color: var(--text-light);
    font-weight: 500;
  }
  .web-address__name { color: var(--accent); font-weight: 600; }

  .holder { position: absolute; left: 373px; top: 157px; color: var(--text-light); }
  .holder__name { font-size: 32px; font-weight: 700; letter-spacing: 0.03em; line-height: 1; }
  .holder__role { font-size: 16px; font-weight: 700; letter-spacing: 0.03em; margin-top: 4px; }

  .contact-list { list-style: none; }
  .contact {
    position: absolute;
    left: 373px;
    font-size: 14px;
    font-weight: 600;
    color: var(--text-light);
    letter-spacing: 0.02em;
    transform: translateY(-50%);
  }
  .contact--phone { top: 264px; }
  .contact--email { top: 303px; }
  .contact--web { top: 342px; }
</style>
</head>
<body>
<main class="canvas">

  <section class="card card--front" aria-label="Card front">
    <svg class="shapes" viewBox="0 0 680 389" aria-hidden="true">
      <path d="M 280 389 A 210 120 0 0 1 560 389" fill="none" stroke="var(--accent)" stroke-width="1.6" opacity="0.8"/>
    </svg>
    <div class="motif" role="img" aria-label="Faint decorative brand motif"></div>
    <div class="brand">
      <span class="brand__mark"></span>
      <span class="brand__name">PineHarbor</span>
    </div>
    <p class="web-address">www.<span class="web-address__name">pineharbor</span>.com</p>
  </section>

  <section class="card card--back" aria-label="Card back">
    <svg class="shapes" viewBox="0 0 680 389" aria-hidden="true">
      <circle cx="581" cy="340" r="280" fill="none" stroke="var(--accent)" stroke-width="2"/>
      <circle cx="581" cy="342" r="274" fill="var(--panel)"/>
      <line x1="373" y1="228" x2="617" y2="228" stroke="var(--rule)" stroke-width="1"/>
      <g class="icon icon--phone">
        <line x1="326" y1="264" x2="368" y2="264" stroke="var(--rule)" stroke-width="1"/>
        <circle cx="310" cy="264" r="15" fill="var(--accent)" stroke="var(--card-mid)" stroke-width="2"/>
        <circle cx="326" cy="264" r="2.5" fill="var(--card-dark)"/>
        <path d="M304 257 q-2 6 4 12 q6 6 12 4 l1-4 -4-2 -2 2 q-4-2-7-7 l2-2 -2-4 z" fill="var(--text-light)"/>
      </g>
      <g class="icon icon--email">
        <line x1="326" y1="303" x2="368" y2="303" stroke="var(--rule)" stroke-width="1"/>
        <circle cx="310" cy="303" r="15" fill="var(--accent)" stroke="var(--card-mid)" stroke-width="2"/>
        <circle cx="326" cy="303" r="2.5" fill="var(--card-dark)"/>
        <rect x="302" y="297" width="16" height="11" fill="var(--text-light)"/>
        <path d="M302 297 l8 6 8-6" fill="none" stroke="var(--accent)" stroke-width="1.3"/>
      </g>
      <g class="icon icon--web">
        <line x1="326" y1="342" x2="368" y2="342" stroke="var(--rule)" stroke-width="1"/>
        <circle cx="310" cy="342" r="15" fill="var(--accent)" stroke="var(--card-mid)" stroke-width="2"/>
        <circle cx="326" cy="342" r="2.5" fill="var(--card-dark)"/>
        <g fill="none" stroke="var(--text-light)" stroke-width="1.3">
          <circle cx="310" cy="342" r="8"/>
          <ellipse cx="310" cy="342" rx="3.5" ry="8"/>
          <line x1="302" y1="342" x2="318" y2="342"/>
        </g>
      </g>
    </svg>
    <div class="motif" role="img" aria-label="Faint decorative brand motif"></div>
    <div class="brand">
      <span class="brand__mark"></span>
      <span class="brand__name">PineHarbor</span>
    </div>
    <div class="holder">
      <h1 class="holder__name">ELENA MARSH</h1>
      <p class="holder__role">OWNER</p>
    </div>
    <ul class="contact-list">
      <li class="contact contact--phone">014.555.0192</li>
      <li class="contact contact--email">info@pineharbormail.com</li>
      <li class="contact contact--web">www.pineharbor.com</li>
    </ul>
  </section>

</main>
</body>
</html>
```